Business Card Design

I need a business card for my corporation. We are a fast food Mexican Taqueria located in San Jose, CA. I want the cards to include our business logo. The cards need to be simple but elegant. Our theme through out our locations is a beach feel atmosphere. I would like to see cards with a beach feeling. Our website is tacoslapalmera.net and it would be great if the cards matched our website.

Industry/Entity Type

Business

Contact Information for Business Card

Marisol Fuentes, VP
2417 Cedar Brook Ave
San Jose, CA 95482
Direct: 4087326159

```html
<!DOCTYPE html>
<html lang="en">
<head>
<meta charset="utf-8">
<title>La Palmera – Business Card</title>
<link href="https://fonts.googleapis.com/css2?family=Fredoka:wght@500;600&display=swap" rel="stylesheet">
<style>
  :root {
    --page: #e9e4da;
    --card-cream: #f7f3e8;
    --sign-cream: #f1e8d2;
    --sign-edge: #8a6a45;
    --post: #d9b07a;
    --brand-red: #b3141c;
    --sky: #bfe3f3;
    --sea: #3fb6cf;
    --foam: #f4f7f6;
    --sand: #efe9dc;
  }
  * { box-sizing: border-box; margin: 0; padding: 0; }
  html, body { width: 1200px; height: 900px; overflow: hidden; }
  body {
    background: var(--page);
    font-family: "Fredoka", "Trebuchet MS", sans-serif;
    position: relative;
  }
  .card {
    position: absolute;
    width: 700px;
    height: 400px;
    border-radius: 4px;
    overflow: hidden;
    box-shadow: 0 6px 18px rgba(60, 45, 25, 0.25);
    background: var(--card-cream);
  }
  .card--front { left: 200px; top: 40px; }
  .card--back { left: 300px; top: 460px; }

  .beach-scene {
    position: absolute;
    inset: 0;
    background: linear-gradient(180deg,
      var(--sky) 0%, #e6f4fa 30%, var(--sea) 36%, #2aa7c4 50%,
      var(--foam) 62%, var(--sand) 100%);
  }
  .beach-band {
    position: absolute;
    left: 0; right: 0; top: 40px; height: 220px;
    background: linear-gradient(180deg,
      rgba(247,243,232,0) 0%, #d9edf5 20%, #bfe2ee 45%,
      #f2f5f3 65%, rgba(247,243,232,0) 100%);
  }

  .sign-post {
    position: absolute;
    background: var(--post);
  }
  .card--front .sign-post { left: 330px; top: 0; width: 40px; height: 400px; }
  .card--back .sign-post { left: 205px; top: 0; width: 40px; height: 400px; }

  .sign-board {
    position: absolute;
    background: var(--sign-cream);
    border: 8px solid var(--sign-edge);
    display: flex;
    align-items: center;
    justify-content: center;
  }
  .card--front .sign-board { left: 170px; top: 60px; width: 380px; height: 210px; }
  .card--back .sign-board { left: 70px; top: 100px; width: 300px; height: 170px; }

  .brand-name {
    color: var(--brand-red);
    font-weight: 600;
    line-height: 1;
    white-space: nowrap;
  }
  .card--front .brand-name { font-size: 62px; }
  .card--back .brand-name { font-size: 48px; }

  .contact {
    position: absolute;
    right: 40px;
    top: 90px;
    color: var(--brand-red);
    font-weight: 600;
    text-align: right;
  }
  .contact__name { font-size: 28px; line-height: 1.1; }
  .contact__title { font-size: 15px; margin-top: 2px; }
  .contact__line {
    display: flex;
    justify-content: flex-end;
    align-items: center;
    gap: 10px;
    font-size: 16px;
    margin-top: 22px;
  }
  .contact__line svg { width: 16px; height: 16px; fill: var(--brand-red); }
  .contact__city {
    position: absolute;
    right: 66px;
    top: 300px;
    color: var(--brand-red);
    font-weight: 600;
    font-size: 16px;
  }
</style>
</head>
<body>

<section class="card card--front">
  <div class="beach-scene" role="img" aria-label="Beach photograph with blue sky, turquoise sea and white surf"></div>
  <div class="sign-post"></div>
  <div class="sign-board">
    <span class="brand-name">La Palmera</span>
  </div>
</section>

<section class="card card--back">
  <div class="beach-band" role="img" aria-label="Faded beach photograph with sky, sea and surf"></div>
  <div class="sign-post"></div>
  <div class="sign-board">
    <span class="brand-name">La Palmera</span>
  </div>

  <div class="contact">
    <div class="contact__name">Marisol Fuentes</div>
    <div class="contact__title">Vice President</div>
    <div class="contact__line">
      <span>408 732 6159</span>
      <svg viewBox="0 0 24 24" aria-hidden="true"><path d="M6.6 10.8a15 15 0 0 0 6.6 6.6l2.2-2.2a1 1 0 0 1 1-.25 11.4 11.4 0 0 0 3.6.57 1 1 0 0 1 1 1V20a1 1 0 0 1-1 1A17 17 0 0 1 3 4a1 1 0 0 1 1-1h3.5a1 1 0 0 1 1 1c0 1.25.2 2.45.57 3.6a1 1 0 0 1-.25 1z"/></svg>
    </div>
    <div class="contact__line">
      <span>2417 Cedar Brook Ave</span>
      <svg viewBox="0 0 24 24" aria-hidden="true"><path d="M12 3 2 12h3v8h5v-5h4v5h5v-8h3z"/></svg>
    </div>
  </div>
  <div class="contact__city">San Jose, CA 95482</div>
</section>

</body>
</html>
```